Beef 100 % Cooked Ready to Eat in a Metal Can

Design a label for a Beef Product 100 % Pure ,Cooked and ready to eat , Be sold in Africa . The label to be in English and French , Or English and Portuguese . Need either a photo or a drawing showing a Bull or Cow .

BRAND Name of the product is " 100% BEEF
Plus + Picture of a Bull or Cow and after to expand Range to include 100 % Mutton , The label should be easy to reproduce and Art work in BALCK AND WHITE for point of sale POSTERS for Advertising . T Shirts ect
Updates

Check out the updated Brief ,and Maybe I will in crease the Budget !

Target Market(s)

African People , Children , illiterate ,Some of the target People who Can read and some can't , From Age 16 - 40 males and female

Image /drawing /or Photo of Bull Or Cow must be Prominent ,

The word 100 % BEEF . Most People can Understand even the ones that cat read

Background color should be stand out form Competitors

Industry/Entity Type

Advertising

Font styles to use
Sans Serif

Colors

Designer to choose colors to be used in the design.

Requirements
Must have

• Recognizable ,easy to remember , Symbols , Image +100%+ Beef = Good Label

Bright Colour ,
Nice to have
• Positive color

Simple Not too Much Copy .

Tin Will Have Ingredients in Small and Bar code in Small .
Should not have
• Modern look .as for Traditional ,Market ,

```html
<!DOCTYPE html>
<html lang="en">
<head>
<meta charset="utf-8">
<title>100% Beef – Can Label</title>
<link href="https://fonts.googleapis.com/css2?family=Archivo+Black&family=Arimo:wght@400&display=swap" rel="stylesheet">
<style>
  :root {
    --backdrop: #d6d6d6;
    --label-white: #ffffff;
    --band-grey: #a9a9a9;
    --band-grey-light: #d4d4d4;
    --frame-grey: #7d7d7d;
    --ribbon-grey: #b3b3b3;
    --ribbon-shade: #8f8f8f;
    --brand-green: #3f6b34;
    --brand-green-light: #6f9a5e;
    --ink: #0d0d0d;
  }
  html, body {
    margin: 0;
    padding: 0;
    width: 897px;
    height: 1200px;
    overflow: hidden;
    background: var(--backdrop);
  }
  .canvas {
    position: relative;
    width: 897px;
    height: 1200px;
  }
  .label {
    position: absolute;
    left: 180px;
    top: 225px;
    width: 530px;
    height: 775px;
    background: var(--label-white);
    overflow: hidden;
  }
  .label-art {
    position: absolute;
    inset: 0;
  }
  .brand-title {
    font-family: "Archivo Black", "Arial Black", sans-serif;
    fill: var(--ink);
  }
  .info-panel {
    position: absolute;
    left: 23px;
    top: 485px;
    width: 483px;
    height: 150px;
    box-sizing: border-box;
    border: 1.5px solid rgba(255,255,255,0.85);
    border-radius: 4px;
    padding: 12px 6px;
    color: #ffffff;
    font-family: "Arimo", Arial, sans-serif;
    font-size: 19px;
    line-height: 29px;
    text-align: justify;
    letter-spacing: -0.2px;
    overflow: hidden;
  }
</style>
</head>
<body>
<main class="canvas">
  <section class="label">
    <svg class="label-art" width="530" height="775" viewBox="0 0 530 775" xmlns="http://www.w3.org/2000/svg">
      <defs>
        <linearGradient id="ribbonFill" x1="0" y1="0" x2="0" y2="1">
          <stop offset="0" stop-color="#c4c4c4"/>
          <stop offset="1" stop-color="#9a9a9a"/>
        </linearGradient>
        <linearGradient id="photoTones" x1="0" y1="0" x2="1" y2="0">
          <stop offset="0" stop-color="#2d6a2a"/>
          <stop offset="0.2" stop-color="#2a241d"/>
          <stop offset="0.5" stop-color="#3a2c20"/>
          <stop offset="0.7" stop-color="#c23a45"/>
          <stop offset="1" stop-color="#e6e6e6"/>
        </linearGradient>
        <clipPath id="shieldInner">
          <path d="M100 22 H444 V270 A172 172 0 0 1 100 270 Z"/>
        </clipPath>
      </defs>

      <rect class="stripe-grey" x="0" y="40" width="530" height="20" fill="var(--band-grey)"/>
      <rect class="stripe-green" x="0" y="75" width="530" height="6" fill="var(--brand-green)"/>

      <path class="shield-frame" d="M92 12 H452 Q458 12 458 18 V272 A186 186 0 0 1 86 272 V18 Q86 12 92 12 Z" fill="var(--frame-grey)"/>
      <path class="shield-face" d="M100 22 H444 V270 A172 172 0 0 1 100 270 Z" fill="var(--label-white)"/>

      <g clip-path="url(#shieldInner)">
        <rect x="100" y="268" width="344" height="190" fill="url(#photoTones)" role="img" aria-label="Photo of a cow beside cuts of raw red beef with parsley on a green swoosh"/>
      </g>

      <path class="ribbon-tail" d="M22 170 H92 V285 H22 L38 228 Z" fill="var(--ribbon-shade)"/>
      <path class="ribbon-tail" d="M508 170 H452 V285 H508 L492 228 Z" fill="var(--ribbon-shade)"/>
      <rect class="ribbon-tail-face" x="30" y="172" width="62" height="108" fill="var(--ribbon-grey)" opacity="0.7"/>
      <rect class="ribbon-tail-face" x="452" y="172" width="48" height="108" fill="var(--ribbon-grey)" opacity="0.7"/>

      <rect class="ribbon" x="80" y="145" width="376" height="115" fill="url(#ribbonFill)"/>
      <rect x="80" y="145" width="376" height="6" fill="#dcdcdc"/>

      <text class="brand-title" x="155" y="123" font-size="82" textLength="230" lengthAdjust="spacingAndGlyphs">100%</text>
      <text class="brand-title" x="140" y="242" font-size="112" textLength="260" lengthAdjust="spacingAndGlyphs">BEEF</text>

      <rect class="info-band" x="0" y="465" width="530" height="195" fill="var(--brand-green)"/>

      <rect class="stripe-green" x="0" y="660" width="530" height="8" fill="var(--brand-green-light)"/>
      <rect class="stripe-grey" x="0" y="700" width="530" height="20" fill="var(--band-grey)"/>
      <rect class="stripe-grey-light" x="0" y="730" width="530" height="8" fill="var(--band-grey-light)"/>
    </svg>

    <div class="info-panel">Text or Image here <span lang="fr">Texte ou image ici</span> Text or Image here <span lang="fr">Texte ou image ici</span> Text or Image here <span lang="fr">Texte ou image ici</span> Text or Image here <span lang="fr">Texte ou image ici</span> Text or Image here <span lang="fr">Texte ou image ici</span></div>
  </section>
</main>
</body>
</html>
```